Book Cover - For Best Selling Diet

Hi
Book cover required for a diet book being marketed to become a best seller
For best quality, image will be 2820 pixels on the shortest side and 4500 pixels on the longest side .
The book name : Bright Morning Plan
By Corinna Plett
( will add in the extra text once we see design - top and bottom subtitle )
I do not want a photo of a person on the book.
PLEASE SEE " THE 9 STEP FRAME" by Ned Galbury as an example of solid style and I also love Quiet Ledger for the font.
Branding Colours:
#F26432
#A4195C
#A7D8CC
Font that runs through our brand is : helvetica neue
This is for a book that will be marketed for #1 bestseller - So please only quality
designs that are designed in a unique style.
Thanks
Target Market(s)
Busy Working Mums, Affluent, 30+ .
Look and feel

```html
<!DOCTYPE html>
<html lang="en">
<head>
<meta charset="utf-8">
<title>Bright Morning Plan – Book Cover</title>
<link rel="stylesheet" href="https://fonts.googleapis.com/css2?family=Inter:wght@200;300&display=swap">
<style>
  :root {
    --brand-orange: #F26432;
    --brand-magenta: #A4195C;
    --brand-mint: #A7D8CC;
    --warm-rose: #C8285A;
    --stage: #1c1c1e;
    --title-white: #ffffff;
  }
  html, body {
    margin: 0;
    padding: 0;
    width: 1200px;
    height: 1031px;
    overflow: hidden;
    background: var(--stage);
  }
  .canvas {
    position: relative;
    width: 1200px;
    height: 1031px;
  }
  .book-cover {
    position: absolute;
    left: 305px;
    top: 45px;
    width: 590px;
    height: 940px;
    background: var(--brand-magenta);
    overflow: hidden;
    box-shadow: 0 10px 40px rgba(0,0,0,0.5);
  }
  .cover-illustration {
    position: absolute;
    left: 110px;
    right: 60px;
    top: 0;
    bottom: 0;
    background: linear-gradient(180deg, var(--brand-orange) 0%, var(--warm-rose) 75%, var(--brand-magenta) 100%);
  }
  .seller-badge {
    position: absolute;
    left: 128px;
    top: 150px;
    width: 96px;
    height: 96px;
    border-radius: 50%;
    background: var(--brand-mint);
  }
  .title {
    position: absolute;
    left: 70px;
    right: 10px;
    top: 290px;
    margin: 0;
    font-family: "Inter", "Helvetica Neue", Arial, sans-serif;
    font-weight: 200;
    font-size: 100px;
    line-height: 1.0;
    letter-spacing: 0;
    text-align: center;
    color: var(--title-white);
    text-transform: uppercase;
  }
  .title span { display: block; }
  .author-band {
    position: absolute;
    left: 0;
    right: 0;
    top: 690px;
    height: 64px;
    background: var(--brand-mint);
    border-top: 3px solid var(--brand-orange);
    border-bottom: 3px solid var(--brand-orange);
    display: flex;
    align-items: center;
    justify-content: center;
  }
  .author {
    font-family: "Inter", "Helvetica Neue", Arial, sans-serif;
    font-weight: 300;
    font-size: 34px;
    color: var(--brand-magenta);
  }
</style>
</head>
<body>
<main class="canvas">
  <section class="book-cover">
    <div class="cover-illustration" role="img" aria-label="Curved waist silhouette illustration in orange to rose tones"></div>
    <div class="seller-badge" aria-hidden="true"></div>
    <h1 class="title"><span>Bright</span><span>Morning</span><span>Plan</span></h1>
    <div class="author-band"><span class="author">Corinna Plett</span></div>
  </section>
</main>
</body>
</html>
```